Postcard Design

I need to have a Table Tent made for our Restaurant. On one side is the Burger Specials and the other side is Happy Hour Drink specials. Our colors are black and white in the restaurant. We need a slightly larger font as our customers are older. The cost of the burgers is $13 each. we are an old school steak house.

Industry/Entity Type

Restaurant

```html
<!DOCTYPE html>
<html lang="en">
<head>
<meta charset="utf-8">
<title>Harlowe's Steakhouse – Table Tent</title>
<link rel="stylesheet" href="https://fonts.googleapis.com/css2?family=Arvo:wght@700&family=Open+Sans:wght@400;700&display=swap">
<style>
  :root {
    --bg: #ecebe8;
    --brand-red: #8f1b1f;
    --deep-red: #6a1215;
    --panel: #d8d9db;
    --ink: #1e1e1e;
    --dark-band: #2a1a17;
    --white: #ffffff;
  }
  * { box-sizing: border-box; margin: 0; padding: 0; }
  html, body { width: 1200px; height: 780px; overflow: hidden; background: var(--bg); }
  .canvas { position: relative; width: 1200px; height: 780px; }

  .card {
    position: absolute; top: 46px; width: 520px; height: 671px;
    background: var(--brand-red); overflow: hidden;
  }
  .card--specials { left: 42px; }
  .card--happy-hour { left: 617px; width: 518px; }

  .photo { position: absolute; left: 0; right: 0; bottom: 0; }
  .photo--burger {
    top: 337px;
    background:
      linear-gradient(180deg, var(--dark-band) 0 4%, transparent 14%),
      radial-gradient(ellipse at 55% 70%, #6b4a2e 0%, #8d7350 25%, transparent 55%),
      linear-gradient(160deg, #5a4636 0%, #c9b79a 35%, #7e8a3d 65%, #3f6a22 100%);
  }
  .photo--drinks {
    top: 345px;
    background:
      radial-gradient(ellipse at 70% 75%, #d23a6a 0%, #b8284f 35%, transparent 65%),
      radial-gradient(ellipse at 10% 40%, #e99a3a 0%, #d67a2a 30%, transparent 60%),
      linear-gradient(180deg, var(--brand-red) 0%, #c76b5a 30%, #e3c8c0 60%, #c0405c 100%);
  }

  .panel {
    position: absolute; background: var(--panel); border-radius: 16px;
    box-shadow: 0 6px 14px rgba(0,0,0,0.35);
  }
  .card--specials .panel { left: 55px; top: 31px; width: 406px; height: 476px; padding-top: 18px; }
  .card--happy-hour .panel { left: 57px; top: 34px; width: 404px; height: 475px; }

  .menu-item { text-align: center; margin-bottom: 6px; }
  .menu-item__name {
    font-family: "Arvo", Georgia, serif; font-weight: 700;
    color: var(--brand-red); font-size: 27px; line-height: 34px;
  }
  .menu-item__desc {
    font-family: "Open Sans", Arial, sans-serif; font-size: 13px; line-height: 16px;
    color: var(--ink); font-weight: 700; padding: 0 24px;
  }
  .menu-item__desc--light { font-weight: 400; }

  .price-badge {
    position: absolute; left: 367px; top: 427px; width: 136px; height: 136px;
    border-radius: 50%; background: var(--brand-red); border: 4px solid var(--white);
    display: flex; align-items: center; justify-content: center;
    font-family: "Arvo", Georgia, serif; font-weight: 700; color: var(--white);
    font-size: 56px; letter-spacing: -1px;
  }
  .price-badge sup { font-size: 30px; vertical-align: 18px; }

  .brand-tag {
    position: absolute; left: 167px; top: 571px; width: 183px; height: 89px;
    background: var(--dark-band);
    display: flex; align-items: center; justify-content: center; text-align: center;
    font-family: "Arvo", Georgia, serif; font-weight: 700; color: var(--white);
    font-size: 21px; line-height: 24px;
  }

  .happy-hour-badge {
    position: absolute; left: 119px; top: 12px; width: 166px; height: 166px;
    border-radius: 50%; background: #1b1b1b;
  }
  .placeholder-note {
    position: absolute; left: 0; right: 0; top: 193px; text-align: center;
    font-family: "Arvo", Georgia, serif; font-weight: 700; color: var(--brand-red);
    font-size: 28px; line-height: 36px;
  }
</style>
</head>
<body>
<div class="canvas">

  <section class="card card--specials" aria-label="Burger specials">
    <div class="photo photo--burger" role="img" aria-label="Photo of a green chile burger with chips, lettuce and onion"></div>
    <div class="panel">
      <div class="menu-item">
        <h2 class="menu-item__name">BBQ Bacon Burger</h2>
        <p class="menu-item__desc">bacon, cheddar, onion rings,<br>bbq sauce, lettuce, tomato,<br>and your choice of side</p>
      </div>
      <div class="menu-item">
        <h2 class="menu-item__name">Green Chile Burger</h2>
        <p class="menu-item__desc">mustard, pickles, tomato, onions,<br>american cheese, hatch green chile,<br>and your choice of side</p>
      </div>
      <div class="menu-item">
        <h2 class="menu-item__name">Grilled Chicken BLT</h2>
        <p class="menu-item__desc menu-item__desc--light">grilled chicken, mozzarella, bacon, lettuce,<br>tomato, mayo, and your choice of side</p>
      </div>
      <div class="menu-item">
        <h2 class="menu-item__name">Shrimp Brochette</h2>
        <p class="menu-item__desc menu-item__desc--light">pepper jack cheese, jalapeno,<br>bacon, served over dirty rice</p>
      </div>
      <div class="menu-item">
        <h2 class="menu-item__name">No Carb Burger</h2>
        <p class="menu-item__desc">mustard, pickles, tomato, onions,<br><span class="menu-item__desc--light">aLettuce leaves as your bun, meat patty, cheese<br>if you like, lettuce, tomato, onions, mayo,<br>mustard and your choice of side</span></p>
      </div>
    </div>
    <div class="price-badge"><sup>$</sup>13</div>
    <div class="brand-tag">Harlowe's<br>Steakhouse</div>
  </section>

  <section class="card card--happy-hour" aria-label="Happy hour drinks">
    <div class="photo photo--drinks" role="img" aria-label="Photo of colourful cocktails with ice and mint"></div>
    <div class="panel">
      <div class="happy-hour-badge" role="img" aria-label="Happy hour stamp emblem"></div>
      <p class="placeholder-note">(space for<br>happy hour drinks<br>which i do not have)</p>
    </div>
  </section>

</div>
</body>
</html>
```